Web page design/layout for dog breeder

We are looking for a new layout/design for our current web page. Current web pages can be found at http://ruddyhound.sitefold.com.

We recently uploaded the PTR Kennel of Renown banner that we would like to have displayed on the home page.

```html
<!DOCTYPE html>
<html lang="en">
<head>
<meta charset="utf-8">
<title>Ruddyhound Kennels</title>
<link rel="stylesheet" href="https://fonts.googleapis.com/css2?family=Oswald:wght@400;500&family=Arimo:wght@400;700&display=swap">
<style>
:root{
  --ink:#111111;
  --text:#555555;
  --white:#ffffff;
  --band:#000000;
  --footer:#2c2c2c;
  --field:#f0f0f0;
  --rule:#d6d6d6;
  --link:#1a5fb4;
  --puppy-a:#8fa86a;
  --puppy-b:#b0733f;
}
*{margin:0;padding:0;box-sizing:border-box}
html,body{width:1200px;height:1080px;overflow:hidden;background:var(--white)}
body{position:relative;font-family:"Arimo",Arial,sans-serif;color:var(--text)}
.abs{position:absolute}
.brand{left:183px;top:62px;font-family:"Oswald",sans-serif;font-weight:500;font-size:27px;letter-spacing:1px;color:var(--ink);line-height:1}
.social-sq{top:22px;width:28px;height:28px;background:var(--ink)}
.search{left:818px;top:22px;width:200px;height:28px;border:1px solid #e4e4e4;background:var(--white);display:flex;align-items:center}
.search span{flex:1;font-size:8px;color:#777;padding-left:8px}
.search .btn{width:29px;height:28px;background:#e8e8e8;display:flex;align-items:center;justify-content:center}
.phone{right:222px;top:64px;font-family:"Oswald",sans-serif;font-size:22px;color:var(--ink);line-height:28px}
.phone-ico{left:991px;top:64px;width:27px;height:27px;background:var(--ink);display:flex;align-items:center;justify-content:center}
.nav{left:0;top:117px;width:1200px;height:44px;background:var(--band)}
.nav ul{list-style:none;position:absolute;left:189px;top:12px;display:flex;gap:28px}
.nav li{font-family:"Oswald",sans-serif;font-size:15px;color:var(--white);line-height:22px;text-transform:uppercase}
.nav li.on{background:var(--white);color:var(--ink);padding:0 8px}
.slider{left:183px;top:194px;width:582px;height:267px;border:2px solid var(--white);box-shadow:0 0 4px rgba(0,0,0,.35);background:linear-gradient(180deg,var(--puppy-a) 0%,#a9b986 40%,var(--puppy-b) 55%,#9fb07a 75%,#c3c8a6 100%)}
.arrow{width:37px;height:37px;background:#1d1d1d;display:flex;align-items:center;justify-content:center}
.dot{width:10px;height:10px;border-radius:50%;border:1.5px solid var(--white)}
.dot.on{background:var(--ink);border-color:var(--ink)}
.finder{left:797px;top:194px;width:221px;height:267px;background:var(--band);padding:18px 19px}
.finder h2{font-family:"Oswald",sans-serif;font-weight:400;font-size:24px;line-height:29px;color:var(--white)}
.field{width:184px;height:28px;background:var(--white);font-size:8px;color:#666;padding-left:12px;line-height:28px;margin-top:15px;position:relative}
.field:first-of-type{margin-top:15px}
.field .dd{position:absolute;right:2px;top:2px;width:24px;height:24px;background:var(--band);display:flex;align-items:center;justify-content:center}
.finder .go{margin-top:15px;width:67px;height:28px;background:#e4e4e4;font-family:"Oswald",sans-serif;font-size:13px;color:var(--ink);text-align:center;line-height:28px}
h3.sec{font-family:"Oswald",sans-serif;font-weight:400;font-size:19px;color:var(--ink);line-height:1}
.welcome{left:183px;top:533px;width:582px;font-size:10.4px;line-height:17.2px;text-align:justify}
.welcome p{margin-bottom:17px}
.welcome b{color:var(--ink)}
.welcome a{color:var(--link);font-weight:700;text-decoration:none}
.listing{left:797px;top:541px;width:221px;height:251px;background:linear-gradient(160deg,#cdb79a 0%,#8f6a4a 45%,#a26c3f 65%,#b9a98d 100%)}
.listing .sm{width:20px;height:21px;background:var(--white);top:71px;display:flex;align-items:center;justify-content:center}
.listing .cap{left:0;bottom:0;width:221px;height:86px;background:rgba(20,20,20,.85);padding:6px 14px;color:var(--white)}
.cap .nm{font-family:"Oswald",sans-serif;font-size:13px;line-height:18px}
.cap .ds{font-size:8.5px;line-height:14px;margin-top:3px}
.cap .meta{font-size:8.5px;font-weight:700;margin-top:8px;display:flex;gap:22px;align-items:center}
.rule{left:183px;top:828px;width:835px;height:1px;background:var(--rule)}
.tile{top:878px;width:82px;height:82px;background:linear-gradient(180deg,#2a2a2a,#000);box-shadow:0 8px 8px -4px rgba(0,0,0,.45)}
.sblock{top:882px}
.sblock h4{font-size:17px;font-weight:700;color:var(--ink);line-height:20px}
.sblock .sub{font-size:11.5px;color:var(--ink);line-height:15px}
.sblock .row{display:flex;align-items:center;gap:4px;margin-top:8px}
.sblock .btn{height:12px;padding:0 4px;border:1px solid #a9bcd6;background:#eef2f8;font-size:7.5px;color:#3b5a8c;line-height:10px}
.sblock .cnt{height:12px;padding:0 4px;border:1px solid #ccc;font-size:7.5px;line-height:10px;color:#333}
.sblock .note{font-size:8px;color:var(--ink);margin-top:6px}
.up{left:581px;top:999px;width:38px;height:38px;border-radius:50%;background:var(--band);display:flex;align-items:center;justify-content:center;z-index:2}
.footer{left:0;top:1020px;width:1200px;height:60px;background:var(--footer);color:var(--white);font-size:10.5px}
.footer .copy{position:absolute;left:183px;top:25px}
.footer ul{position:absolute;right:182px;top:25px;list-style:none;display:flex;gap:16px}
</style>
</head>
<body>

<header>
  <div class="abs brand">RUDDYHOUND KENNELS</div>
  <div class="abs social-sq" style="left:746px" aria-label="Facefold page"></div>
  <div class="abs social-sq" style="left:782px" aria-label="Chirper page"></div>
  <div class="abs search"><span>to search, type and hit enter</span>
    <div class="btn"><svg width="16" height="16" viewBox="0 0 16 16"><circle cx="10" cy="6" r="4.5" fill="none" stroke="#111" stroke-width="1.8"/><line x1="7" y1="9" x2="2" y2="14" stroke="#111" stroke-width="2.2" stroke-linecap="round"/></svg></div>
  </div>
  <div class="abs phone">555-010-4477</div>
  <div class="abs phone-ico"><svg width="15" height="15" viewBox="0 0 24 24"><path fill="#fff" d="M6.6 10.8c1.4 2.8 3.8 5.1 6.6 6.6l2.2-2.2c.3-.3.7-.4 1-.2 1.1.4 2.3.6 3.6.6.6 0 1 .4 1 1V20c0 .6-.4 1-1 1C10.6 21 3 13.4 3 4c0-.6.4-1 1-1h3.5c.6 0 1 .4 1 1 0 1.3.2 2.5.6 3.6.1.3 0 .7-.2 1z"/></svg></div>
</header>

<nav class="abs nav">
  <ul>
    <li class="on">Home</li><li>Our Dogs</li><li>Upcoming Litter</li><li>Contact Us</li><li>Photo Gallery</li><li>Past Litters</li>
  </ul>
</nav>

<section class="abs slider" role="img" aria-label="Photo of a red puppy walking across a green grass field">
  <div class="abs arrow" style="left:13px;top:113px"><svg width="10" height="14" viewBox="0 0 10 14"><path d="M8 1L2 7l6 6" fill="none" stroke="#fff" stroke-width="1.6"/></svg></div>
  <div class="abs arrow" style="left:526px;top:113px"><svg width="10" height="14" viewBox="0 0 10 14"><path d="M2 1l6 6-6 6" fill="none" stroke="#fff" stroke-width="1.6"/></svg></div>
  <div class="abs" style="left:266px;top:242px;display:flex;gap:8px"><div class="dot on"></div><div class="dot"></div><div class="dot"></div></div>
</section>

<aside class="abs finder">
  <h2>Find an Awesome Petsitter Near You</h2>
  <div class="field" style="margin-top:17px">All Pet Sitters</div>
  <div class="field">Any Location</div>
  <div class="field">Service Type<div class="dd"><svg width="10" height="6" viewBox="0 0 10 6"><path d="M1 1l4 4 4-4" fill="none" stroke="#fff" stroke-width="1.4"/></svg></div></div>
  <div class="go">SEARCH</div>
</aside>

<h3 class="abs sec" style="left:183px;top:493px">Welcome to Ruddyhound Kennels</h3>
<h3 class="abs sec" style="left:797px;top:493px">Featured Listings</h3>

<div class="abs welcome">
  <p>We were introduced to our first vizsla on a hunting trip in the mid 1990s.&nbsp; We were impressed by this medium sized dog that had a superior nose and high-class hunting ability. And so it began, our first vizsla, Max, joined our family in 1999.</p>
  <p>Our vizslas have always been a part of our family and spend many hours each year in the field with us as our hunting companions. We participate in NKR hunt tests and field trials with our vizsla family.&nbsp; We have been members of the Ruddy Pointer Club of America, Prairie Pointer Club, Riverbend Pointer Club and Platte Valley Pointer Club.&nbsp; Dale has also served as the Ruddy Pointer Club of America Rescue Coordinator for Iowa and Nebraska and served as the Spring Field Trial Chair for the Prairie Pointer Club.</p>
  <p>We are dedicated to raising, training and breeding vizslas to produce healthy dogs that showcase their power and hunting drive along with their trainability and temperament that will excel both in the field and in the show ring.&nbsp; Any of our breedings are done with the purpose of improving the breed.&nbsp; Our dogs are proven in the field with all of the recommended health checks completed before breeding them.</p>
  <p style="margin-bottom:0"><b>To learn more about our vizsla family, click on the above links.</b><br>Be sure to check us out on Facefold at <a>https://www.facefold.com/ruddyhoundkennels</a></p>
</div>

<article class="abs listing" role="img" aria-label="Photo of a young child playing with two red puppies">
  <div class="abs sm" style="left:0"><svg width="6" height="9" viewBox="0 0 6 9"><path d="M5 1L1.5 4.5 5 8" fill="none" stroke="#111" stroke-width="1.2"/></svg></div>
  <div class="abs sm" style="right:0"><svg width="6" height="9" viewBox="0 0 6 9"><path d="M1 1l3.5 3.5L1 8" fill="none" stroke="#111" stroke-width="1.2"/></svg></div>
  <div class="abs cap">
    <div class="nm">John Doe</div>
    <div class="ds">Lorem Ipsum is simply dummy text of the printing and typesetting industry.</div>
    <div class="meta">
      <span><svg width="8" height="11" viewBox="0 0 8 11" style="vertical-align:-2px;margin-right:4px"><path fill="#fff" d="M4 0a4 4 0 0 0-4 4c0 3 4 7 4 7s4-4 4-7a4 4 0 0 0-4-4zm0 5.5A1.5 1.5 0 1 1 4 2.5a1.5 1.5 0 0 1 0 3z"/></svg>Orlando, FL</span>
      <span><svg width="10" height="9" viewBox="0 0 10 9" style="vertical-align:-1px;margin-right:4px"><path fill="#fff" d="M0 3.5h4V1l3.5 3.5L4 8V5.5H0z"/><path d="M6 .5h3.5v8H6" fill="none" stroke="#fff" stroke-width="1"/></svg>Posted 5 days ago</span>
    </div>
  </div>
</article>

<div class="abs rule"></div>

<section>
  <div class="abs tile" style="left:311px" aria-label="Facefold"></div>
  <div class="abs sblock" style="left:410px">
    <h4>We’re on Facefold</h4>
    <div class="sub">Like us to see our update!</div>
    <div class="row"><span class="btn">Like</span><span class="cnt">117</span></div>
    <div class="note">Be the frist of your friends to like this.</div>
  </div>
  <div class="abs tile" style="left:667px" aria-label="Chirper"></div>
  <div class="abs sblock" style="left:766px">
    <h4>We’re on Chirper</h4>
    <div class="sub">Like us to see our update!</div>
    <div class="row"><span class="btn">Chirp</span><span class="cnt">692</span></div>
    <div class="note">Be the frist of your friends to like this.</div>
  </div>
</section>

<div class="abs up"><svg width="14" height="8" viewBox="0 0 14 8"><path d="M1 7l6-6 6 6" fill="none" stroke="#fff" stroke-width="1.6"/></svg></div>

<footer class="abs footer">
  <div class="copy">Copyright © 2014 Ruddyhound &nbsp;|&nbsp; All Rights Reserved</div>
  <ul><li>Home</li><li>Our Dogs</li><li>Upcoming Litter</li><li>Contact us</li><li>Photo Gallery</li><li>Past Litters</li></ul>
</footer>

</body>
</html>
```